Flyer Design

I recently got a website designed by Pagecraft - www.tidynestliving.com.au

I own an organisational business. We help people to simplify their homes which in turn, creates a more balanced and healthy life. We offer de-clutter services for pantries, wardrobes, linen cupboards, home offices, and anywhere you need a bit of organisation. We can help you with de-cluttering and property styling that will help to sell your home. In addition, we provide help with moving, packing and unpacking, or even downsizing. With our keen eye for detail and passion for interior design, we will not only provide a practical solution, but a wonderful design element to your home. Tidy Nest Living is a proud member of the Southern Guild of Certified Space Planners Inc.

Can I please use the logo off my website. I have also put it below.

Industry/Entity Type

Business

```html
<!DOCTYPE html>
<html lang="en">
<head>
<meta charset="utf-8">
<title>Tidy Nest Living Flyer</title>
<link href="https://fonts.googleapis.com/css2?family=Lato:wght@400;700&family=Roboto+Condensed:wght@700&display=swap" rel="stylesheet">
<style>
  :root {
    --ink: #2b2a2c;
    --ink-deep: #1f1e20;
    --cyan: #3fbfd8;
    --cyan-dark: #1d9fbb;
    --white: #ffffff;
    --paper: #f2f2f2;
    --text: #2e2e2e;
  }
  * { margin: 0; padding: 0; box-sizing: border-box; }
  html, body { width: 864px; height: 1200px; overflow: hidden; background: var(--white); }
  .flyer {
    position: relative; width: 864px; height: 1200px; overflow: hidden;
    background: linear-gradient(180deg, #ffffff 0%, #eeeeee 100%);
    font-family: "Lato", Arial, sans-serif; color: var(--text);
  }
  .hero { position: absolute; left: 0; top: 0; width: 864px; height: 680px; display: block; }
  .brand {
    position: absolute; left: 34px; top: 34px; display: flex; align-items: center; gap: 14px;
  }
  .brand-mark { width: 38px; height: 38px; background: var(--cyan); }
  .brand-name {
    font-family: "Lato", Arial, sans-serif; font-weight: 700; font-size: 30px;
    letter-spacing: 1.5px; text-transform: uppercase; color: var(--white);
  }
  .headline {
    position: absolute; left: 0; top: 685px; width: 864px; height: 94px;
    background: linear-gradient(180deg, var(--cyan) 0%, var(--cyan-dark) 100%);
    display: flex; align-items: center; justify-content: center;
  }
  .headline h1 {
    font-family: "Roboto Condensed", "Arial Narrow", sans-serif; font-weight: 700;
    font-size: 62px; color: var(--white); letter-spacing: 0.5px;
  }
  .about-tab {
    position: absolute; left: 0; top: 787px; width: 224px; height: 42px;
    background: var(--ink); clip-path: polygon(0 0, 100% 0, 92% 100%, 0 100%);
    padding-left: 30px; display: flex; align-items: center;
  }
  .about-tab h2, .offer-ribbon h2 {
    font-family: "Roboto Condensed", "Arial Narrow", sans-serif; font-weight: 700;
    font-size: 32px; color: var(--cyan); text-transform: uppercase;
  }
  .about-text {
    position: absolute; left: 32px; top: 850px; width: 372px;
    font-size: 20.5px; line-height: 27px; text-align: justify; hyphens: auto; color: var(--text);
  }
  .offer-shield {
    position: absolute; left: 453px; top: 787px; width: 390px; height: 298px;
    background: linear-gradient(180deg, var(--ink) 0%, var(--ink-deep) 100%);
    clip-path: polygon(0 0, 100% 0, 100% 68%, 50% 100%, 0 68%);
  }
  .offer-ribbon {
    position: absolute; left: 433px; top: 822px; width: 431px; height: 46px;
    background: linear-gradient(180deg, var(--cyan) 0%, var(--cyan-dark) 100%);
    display: flex; align-items: center; justify-content: center;
  }
  .offer-ribbon h2 { color: var(--white); }
  .offer-list {
    position: absolute; left: 453px; top: 898px; width: 390px; list-style: none;
    text-align: center; color: var(--white); font-size: 21px; line-height: 27px;
  }
  .offer-list li::before {
    content: ""; display: inline-block; width: 10px; height: 10px; border-radius: 50%;
    background: var(--cyan); margin-right: 8px; vertical-align: 3px;
  }
  .footer {
    position: absolute; left: 0; top: 1120px; width: 864px; height: 80px;
    background: var(--paper); border-top: 4px solid var(--ink);
  }
  .footer-call {
    position: absolute; left: 0; top: 0; width: 480px; height: 76px;
    background: linear-gradient(180deg, var(--cyan) 0%, var(--cyan-dark) 100%);
    clip-path: polygon(0 0, 100% 0, 96% 100%, 0 100%);
    display: flex; align-items: center; padding-left: 30px;
    font-size: 28px; font-weight: 700; color: var(--white);
  }
  .footer-call .phone { color: var(--ink); font-weight: 400; margin-left: 8px; }
  .footer-contact {
    position: absolute; left: 510px; top: 10px; list-style: none;
    font-size: 18px; line-height: 28px; font-weight: 700; color: var(--ink);
  }
  .footer-contact li { display: flex; align-items: center; gap: 10px; }
  .footer-contact svg { width: 16px; height: 16px; }
</style>
</head>
<body>
<div class="flyer">
  <svg class="hero" viewBox="0 0 864 680" xmlns="http://www.w3.org/2000/svg">
    <defs>
      <linearGradient id="roomTone" x1="0" y1="0" x2="1" y2="1">
        <stop offset="0" stop-color="#e9ecee"/>
        <stop offset="0.5" stop-color="#c9d2d8"/>
        <stop offset="1" stop-color="#7d858a"/>
      </linearGradient>
      <linearGradient id="shelfTone" x1="0" y1="0" x2="0" y2="1">
        <stop offset="0" stop-color="#d9d6cf"/>
        <stop offset="1" stop-color="#6b5a4e"/>
      </linearGradient>
    </defs>
    <rect class="hero-backdrop" x="0" y="0" width="864" height="680" fill="#2b2a2c"/>
    <polygon class="hero-photo" role="img" aria-label="Photo of a bright, tidy attic living room with white brick wall, framed prints and a grey chaise"
      points="0,236 272,190 864,282 864,680 0,680" fill="url(#roomTone)"/>
    <polygon class="hero-stripe" points="0,208 272,162 864,256 864,282 272,190 0,236" fill="#3fbfd8"/>
    <polygon class="detail-frame" points="653,84 752,144 752,302 653,362 554,302 554,144" fill="#3fbfd8"/>
    <polygon class="detail-photo" role="img" aria-label="Photo of a styled shelf with framed pictures, books and letter ornaments"
      points="653,98 740,151 740,295 653,348 566,295 566,151" fill="url(#shelfTone)" stroke="#ffffff" stroke-width="4"/>
  </svg>

  <div class="brand">
    <span class="brand-mark"></span>
    <span class="brand-name">Tidy Nest Living</span>
  </div>

  <div class="headline"><h1>UNCLUTTER YOUR LIFE TODAY</h1></div>

  <div class="about-tab"><h2>About Us</h2></div>
  <p class="about-text">We can help you with de-cluttering and property styling that will help to sell your home. In addition, we provide help with moving, packing and unpacking, or even downsizing. With our keen eye for detail and passion for interior design, we will not only provide a practical solution, but a wonderful design element to your home.</p>

  <div class="offer-shield"></div>
  <div class="offer-ribbon"><h2>We Offer</h2></div>
  <ul class="offer-list">
    <li>De-clutter services for pantries</li>
    <li>Wardrobes</li>
    <li>Linen cupboards</li>
    <li>Home offices</li>
  </ul>

  <div class="footer">
    <div class="footer-call">Call us now<span class="phone">0455123987</span></div>
    <ul class="footer-contact">
      <li><svg viewBox="0 0 16 16"><rect x="1" y="3" width="14" height="10" fill="#2b2a2c"/><polyline points="1,3 8,9 15,3" fill="none" stroke="#f2f2f2" stroke-width="1.5"/></svg>hello@tidynestliving.com.au</li>
      <li><svg viewBox="0 0 16 16"><circle cx="8" cy="8" r="7" fill="#2b2a2c"/><ellipse cx="8" cy="8" rx="3" ry="7" fill="none" stroke="#f2f2f2" stroke-width="1"/><line x1="1" y1="8" x2="15" y2="8" stroke="#f2f2f2" stroke-width="1"/></svg>www.tidynestliving.com.au</li>
    </ul>
  </div>
</div>
</body>
</html>
```